PowerPoint Design Project

Design Brief
Corvanta is updating its stationary templates to reflect the company’s position as market leader in smart-location based solutions.
Using the existing Corvanta logo and corporate colours, create an engaging and visually appealing PowerPoint presentation template identity that works when printed on A4 and US Letter sized paper.
The successful designs will complement the current look and feel of the Corvanta website (www.corvanta-example.net) and communicate that Corvanta is a dynamic and modern technology company that is at the cutting edge of innovation.
Corvanta Brand
Corvanta stands for Precision Location Technology. The brand represents both a unique, highly innovative platform product and a mature consulting and support organisation dedicated to delivering solutions to blue-chip customer problems. The orange colour implies creativity while blue evokes trust and a rational approach. “Ubi” is Latin and means “where”, so the brand directly addresses the focus of the company: location. “Sense” can mean that we have sensing technology to support our precision location aware applications and solutions, but also that we make sensible use of location data to improve customer processes.
Corvanta Corporate Profile
Corvanta is a market leader of location-based Smart Factory Solutions which enables companies to optimise their business processes. By keeping track of key assets, Corvanta solutions bring clarity to complex operations in industries while also improving quality and reliability. Corvanta uses a unique combination of advancefd industry knowledge and an experienced team to deliver effective and superior solutions that offer unprecedented visibility, control and accuracy, delivering time and cost savings. Corvanta solutions are easy to implement and flexible to a particular business’s needs, no matter which area of the globe they operate in.
Corvanta offers two location-oriented products; RTLS (Real-time Location Solutions) and Geospatial Systems and operates in a number of industries ranging from manufacturing and utilities to telecommunications and is used by a number of blue chip customers across the world, such as KLT, Skyvane, Groundmole, Fenwick Power, RAL and Nordische Fernmelde.
Corvanta Corporate Colours
Orange:
Pantone 021C
R: 237 / G: 110 / B: 0
C: 0 / M: 53 / Y: 100 / K: 0
Hex #ED6E00
Dark Blue:
Pantone 662C
R: 15 / G: 31 / B: 122
C: 100 / M: 71 / Y: 0 / K:0
Hex #0F1F7A
Light Blue:
Pantone 300C
R: 0 / G: 110 / B: 199
C: 100 / M: 44 / Y: 0 / K:0
Hex #006EC7
Corvanta Corporate Fonts
The preferred font is Tahoma for Title, Topics and Print. In certain situations, Arial is an acceptable alternative.
Target Market(s)
Manufacturing industry, Automotive and Aerospace
Industry/Entity Type
Telecommunications
Look and feel

```html
<!DOCTYPE html>
<html lang="en">
<head>
<meta charset="utf-8">
<title>Corvanta Presentation Template</title>
<link href="https://fonts.googleapis.com/css2?family=Noto+Sans:wght@400;700&family=Carlito:wght@400;700&display=swap" rel="stylesheet">
<style>
  :root {
    --stage: #262626;
    --orange: #ED6E00;
    --amber: #F7B21B;
    --navy: #0F1F7A;
    --footer: #24366f;
    --blue: #006EC7;
    --logo-blue: #2b3f8f;
    --title-grey: #3c3c3c;
    --text-grey: #222;
    --muted: #666;
    --chart-red: #c8141a;
    --box-red: #c40d10;
    --box-edge: #7a0406;
  }
  * { box-sizing: border-box; margin: 0; padding: 0; }
  html, body { width: 1200px; height: 898px; overflow: hidden; background: var(--stage); }
  .canvas { position: relative; width: 1200px; height: 898px; background: var(--stage); }

  .slide {
    position: absolute; width: 550px; height: 414px; overflow: hidden;
    background:
      radial-gradient(ellipse 70% 45% at 45% 55%, rgba(255,255,255,.95), rgba(255,255,255,0) 70%),
      linear-gradient(160deg, #f4f4f4 0%, #e2e3e6 55%, #d4d6da 100%);
    font-family: "Carlito", "Noto Sans", sans-serif;
    box-shadow: 0 2px 8px rgba(0,0,0,.6);
  }
  .slide--cover { left: 35px; top: 26px; }
  .slide--text { left: 617px; top: 26px; }
  .slide--org { left: 35px; top: 463px; }
  .slide--chart { left: 617px; top: 463px; }

  .brand { display: flex; align-items: center; gap: 5px; font-family: "Noto Sans", sans-serif; color: var(--logo-blue); font-weight: 400; }
  .brand__dot { display: inline-block; border-radius: 50%; background: var(--orange); }

  .slide-header {
    position: absolute; left: 0; top: 0; width: 100%; height: 36px;
    background: linear-gradient(180deg, #c9cbce 0%, #e9eaec 55%, #f3f3f4 100%);
    display: flex; align-items: center; justify-content: space-between; padding: 0 8px 0 14px;
  }
  .slide-header__title { font-family: "Noto Sans", sans-serif; font-weight: 700; font-size: 21px; color: var(--title-grey); }
  .slide-header .brand { font-size: 17px; }
  .slide-header .brand__dot { width: 15px; height: 15px; }

  .slide-footer {
    position: absolute; left: 0; bottom: 0; width: 100%; height: 15px;
    background: var(--footer); color: #fff;
    font-family: "Noto Sans", sans-serif; font-weight: 700; font-size: 9px;
    line-height: 15px; padding-left: 6px;
  }
  .slide-number {
    position: absolute; right: 0; bottom: 0; width: 34px; height: 21px;
    background: var(--footer); color: #fff; font-family: "Noto Sans", sans-serif;
    font-weight: 700; font-size: 14px; text-align: center; line-height: 21px;
  }

  /* cover */
  .cover-band { position: absolute; left: 0; top: 0; width: 100%; height: 64px;
    background: linear-gradient(180deg, var(--amber) 0%, #f29a12 60%, var(--orange) 100%); }
  .cover-logo { position: absolute; left: 12px; top: 9px; width: 210px; height: 48px;
    background: linear-gradient(#fff, #eef0f4); border-radius: 6px; padding-left: 12px; }
  .cover-logo .brand { height: 100%; font-size: 32px; gap: 8px; }
  .cover-logo .brand__dot { width: 30px; height: 30px; }
  .cover-title { position: absolute; right: 50px; top: 130px; text-align: right;
    font-family: "Noto Sans", sans-serif; font-weight: 700; font-size: 34px; line-height: 40px; color: var(--title-grey); }
  .cover-meta { position: absolute; right: 52px; text-align: right; font-family: "Noto Sans", sans-serif; font-size: 22px; color: var(--muted); }
  .cover-meta--name { top: 236px; }
  .cover-meta--role { top: 284px; }

  /* statement */
  .statement { position: absolute; left: 30px; right: 30px; top: 100px; text-align: center;
    font-size: 17px; line-height: 22px; color: var(--text-grey); }

  /* org chart */
  .org-title { position: absolute; left: 0; width: 534px; top: 62px; text-align: center; font-size: 14px; color: #1a2a6e; letter-spacing: .2px; }
  .org-lines { position: absolute; left: 0; top: 0; }
  .org-box { position: absolute; background: var(--box-red); border: 1px solid var(--box-edge); border-radius: 3px;
    color: #fff; font-size: 9px; line-height: 11px; text-align: center;
    display: flex; align-items: center; justify-content: center; }

  /* chart */
  .chart { position: absolute; left: 0; top: 36px; }
  .chart-caption { position: absolute; left: 0; width: 100%; top: 340px; text-align: center; font-size: 19px; color: #111; }
</style>
</head>
<body>
<main class="canvas">

  <section class="slide slide--cover">
    <div class="cover-band"></div>
    <div class="cover-logo"><div class="brand"><span class="brand__dot"></span>Corvanta</div></div>
    <h1 class="cover-title">Apresentation<br>Title</h1>
    <p class="cover-meta cover-meta--name">XXXX</p>
    <p class="cover-meta cover-meta--role">XXXX, CEO</p>
    <div class="slide-footer">© 2012 Corvanta Confidential e Proprietary</div>
  </section>

  <section class="slide slide--text">
    <header class="slide-header"><h2 class="slide-header__title">Real Time Location Solutions</h2><div class="brand"><span class="brand__dot"></span>Corvanta</div></header>
    <p class="statement">Corvanta location solutions offer unparalleled scalability to cover complex global operations and a level of precision that can detect the subtlest nuances in industrial environments where objects are constantly on the move. With a proven track record of reliability, our solutions are used in critical commercial operations and cutting edge research programs around the globe.</p>
    <div class="slide-footer">© 2012 Corvanta Confidential e Proprietary</div>
    <div class="slide-number">2</div>
  </section>

  <section class="slide slide--org">
    <header class="slide-header"><h2 class="slide-header__title">Real Time Location Solutions</h2><div class="brand"><span class="brand__dot"></span>Corvanta</div></header>
    <p class="org-title">THE CIVIC INSTITUTE OF PUBLIC STEWARDSHIP</p>
    <svg class="org-lines" width="550" height="414" viewBox="0 0 550 414" fill="none" stroke="#1a2a6e" stroke-width="1">
      <path d="M261 122V140M186 138H219M186 171H202V138M303 156H319V138H335M319 156V171H335M202 156H219"/>
      <path d="M261 173V194H186V204M261 194H334V204M309 233V240M353 254H368M402 218H408V240M309 269V276M309 305V311"/>
    </svg>
    <div class="org-box" style="left:219px;top:91px;width:84px;height:31px">Fellows<br>Board of Directors</div>
    <div class="org-box" style="left:99px;top:124px;width:87px;height:29px">IT Consultant<br>Owen Pritchard</div>
    <div class="org-box" style="left:99px;top:157px;width:87px;height:29px">Director of HR<br>Nora Ellwood</div>
    <div class="org-box" style="left:219px;top:140px;width:84px;height:33px">Martin R. Hale<br>President and CEO</div>
    <div class="org-box" style="left:335px;top:124px;width:98px;height:29px">General Counsel<br>Clara Benning</div>
    <div class="org-box" style="left:335px;top:157px;width:98px;height:29px">Chief Financial Officer<br>Board of Directors</div>
    <div class="org-box" style="left:118px;top:204px;width:136px;height:29px">Director of Fellow Relations<br>Dana Keller</div>
    <div class="org-box" style="left:267px;top:204px;width:135px;height:29px">Director of Project Development<br>Simon Archer</div>
    <div class="org-box" style="left:264px;top:240px;width:89px;height:29px">Project Directors</div>
    <div class="org-box" style="left:368px;top:240px;width:80px;height:29px">Analysts</div>
    <div class="org-box" style="left:264px;top:276px;width:89px;height:29px">Project Advisor</div>
    <div class="org-box" style="left:264px;top:311px;width:89px;height:31px">Research Associates</div>
    <div class="slide-footer">© 2012 Corvanta Confidential e Proprietary</div>
    <div class="slide-number">4</div>
  </section>

  <section class="slide slide--chart">
    <header class="slide-header"><h2 class="slide-header__title">Real Time Location Solutions</h2><div class="brand"><span class="brand__dot"></span>Corvanta</div></header>
    <svg class="chart" width="550" height="300" viewBox="0 0 550 300" role="img" aria-label="Pie chart of annual investment in three segments">
      <defs>
        <linearGradient id="redTop" x1="0" y1="0" x2="0" y2="1"><stop offset="0" stop-color="#e8262b"/><stop offset="1" stop-color="#b80d12"/></linearGradient>
        <linearGradient id="greenTop" x1="0" y1="0" x2="1" y2="1"><stop offset="0" stop-color="#b6e35a"/><stop offset="1" stop-color="#6fb82a"/></linearGradient>
        <linearGradient id="yellowTop" x1="0" y1="0" x2="1" y2="1"><stop offset="0" stop-color="#fff25a"/><stop offset="1" stop-color="#f2b600"/></linearGradient>
      </defs>
      <path d="M285 170L170.1 218.2V243.2L285 195Z" fill="#7e070b"/>
      <path d="M170.1 218.2A150 75 0 0 1 135 170V195A150 75 0 0 0 170.1 243.2Z" fill="#8f0a0e"/>
      <path d="M285 170L170.1 218.2A150 75 0 1 1 435 170Z" fill="url(#redTop)"/>
      <path d="M231.2 277.4A150 75 0 0 1 155.1 253.2V278.2A150 75 0 0 0 231.2 302.4Z" fill="#c98a00"/>
      <path d="M270 205L231.2 277.4A150 75 0 0 1 155.1 253.2Z" fill="url(#yellowTop)"/>
      <path d="M455 185A150 75 0 0 1 278.9 258.9V283.9A150 75 0 0 0 455 210Z" fill="#4d8d1c"/>
      <path d="M305 185L455 185A150 75 0 0 1 278.9 258.9Z" fill="url(#greenTop)"/>
    </svg>
    <p class="chart-caption">Annual Investment Chart</p>
    <div class="slide-footer">© 2012 Corvanta Confidential e Proprietary</div>
    <div class="slide-number">3</div>
  </section>

</main>
</body>
</html>
```